Card for Real Estate Developer

We need a business card design for a Real Estate Development company based in Texas. We focus on retail, apartment and residential development. Our target is predominantly investors looking to us to place their money properly to achieve a significant return. On the other side we sell our services to large retailers as their preferred developer assisting them in locating, building and leasing their real estate.

Target Market(s)

Investors

Industry/Entity Type

Real Estate Development

Contact Information for Business Card

Would like to stay within the company color scheme, while keeping the design moderately simple.

Font styles to use
Other font styles liked:
• per attached document

Requirements
Must have
• Name
• Phone
• Email
• Website
• Logo Prominently Displayed
• Stay within the colors provided in the attached document

```html
<!DOCTYPE html>
<html lang="en">
<head>
<meta charset="UTF-8">
<title>Bexley Development – Business Card</title>
<link href="https://fonts.googleapis.com/css2?family=Cinzel:wght@400&family=Varela+Round&family=Arimo:wght@400&display=swap" rel="stylesheet">
<style>
  :root {
    --stage: #1f1f20;
    --card-dark: #3d3d3f;
    --card-light: #efefef;
    --brand-blue: #4f8fb5;
    --band-edge: #2c2c2e;
    --ink: #3a3a3c;
    --white: #ffffff;
  }
  * { margin: 0; padding: 0; box-sizing: border-box; }
  html, body {
    width: 1200px; height: 800px; overflow: hidden;
    background: var(--stage);
  }
  .stage { position: relative; width: 1200px; height: 800px; }

  .card {
    position: absolute; top: 238px;
    width: 536px; height: 306px;
    overflow: hidden;
    background: var(--card-light);
    box-shadow: 0 6px 18px rgba(0,0,0,0.55);
  }
  .card--front { left: 49px; }
  .card--back  { left: 617px; }

  .card__shapes { position: absolute; inset: 0; width: 100%; height: 100%; }

  /* Wordmark on front */
  .wordmark { position: absolute; text-align: center; font-family: "Cinzel", serif; font-weight: 400; color: var(--white); }
  .card--front .wordmark { left: 29px; width: 240px; top: 120px; }
  .wordmark__name { display: block; font-size: 34px; line-height: 1; letter-spacing: 1px; }
  .wordmark__sub  { display: block; font-size: 14px; letter-spacing: 4.5px; margin-top: 8px; }

  /* Name tag */
  .person {
    position: absolute; left: 77px; top: 233px;
    font-family: "Varela Round", sans-serif; font-size: 27px;
    color: var(--white); line-height: 36px;
  }

  /* Contacts */
  .contact {
    position: absolute; right: 27px;
    font-family: "Arimo", sans-serif; font-size: 13.5px;
    color: var(--white); line-height: 18px; text-align: right;
    white-space: nowrap;
  }
  .contact--phone { top: 88px; }
  .contact--email { top: 142px; }
  .contact--web   { top: 197px; }

  /* Back wordmark */
  .card--back .wordmark { left: 0; width: 100%; top: 80px; color: var(--ink); }
  .card--back .wordmark__name { font-size: 96px; letter-spacing: 2px; }
  .card--back .wordmark__sub  { font-size: 34px; letter-spacing: 11px; margin-top: 14px; padding-left: 11px; }
</style>
</head>
<body>
<main class="stage">

  <section class="card card--front" aria-label="Business card front">
    <svg class="card__shapes" viewBox="0 0 670 382" preserveAspectRatio="none" aria-hidden="true">
      <polygon points="0,0 295,0 431,382 0,382" fill="var(--card-dark)"/>
      <!-- contact bands -->
      <polygon points="347,91 670,91 670,153 380,153" fill="var(--band-edge)"/>
      <polygon points="356,91 670,91 670,153 389,153" fill="var(--brand-blue)"/>
      <polygon points="337,159 670,159 670,222 370,222" fill="var(--band-edge)"/>
      <polygon points="346,159 670,159 670,222 379,222" fill="var(--brand-blue)"/>
      <polygon points="335,226 670,226 670,290 371,290" fill="var(--band-edge)"/>
      <polygon points="344,226 670,226 670,290 380,290" fill="var(--brand-blue)"/>
      <!-- name tag -->
      <rect x="0" y="283" width="73" height="62" fill="var(--brand-blue)"/>
      <rect x="73" y="283" width="3" height="62" fill="#2f6d92"/>
      <circle cx="44" cy="308" r="5" fill="var(--white)"/>
      <path d="M35 322 q9 -12 18 0 z" fill="var(--white)"/>
      <!-- icons -->
      <g fill="var(--white)">
        <rect x="642" y="115" width="14" height="11" rx="1"/>
        <rect x="642" y="184" width="14" height="11" rx="1"/>
        <rect x="642" y="251" width="14" height="12" rx="1"/>
      </g>
      <g fill="var(--brand-blue)">
        <rect x="645" y="118" width="8" height="3"/>
        <path d="M644 186 l5 4 l5 -4 z"/>
        <circle cx="649" cy="257" r="3.5"/>
      </g>
    </svg>

    <div class="wordmark">
      <span class="wordmark__name">BEXLEY</span>
      <span class="wordmark__sub">DEVELOPMENT</span>
    </div>

    <p class="person">Owen Hale</p>

    <p class="contact contact--phone">04 5512 3390</p>
    <p class="contact contact--email">owen@bexleydevelopment.com</p>
    <p class="contact contact--web">www.bexleydevelopment.com</p>
  </section>

  <section class="card card--back" aria-label="Business card back">
    <div class="wordmark">
      <span class="wordmark__name">BEXLEY</span>
      <span class="wordmark__sub">DEVELOPMENT</span>
    </div>
  </section>

</main>
</body>
</html>
```